Pool & Hot Tub Company Need Vehicle Wrap Designs

We need vehicle wrap designs for a Pool & Hot Tub company based in Vancouver, Canada. We do weekly maintenance and repairs. These wraps will be for a 2022 Halvorden Kesta. We are looking for something clean and modern but not boring with a bunch of lines and text. Although we service both pools and hot tubs, this design needs to be hot tub specific. We will be needing future designs for the pool division as well as the repair division, and we would like them all to be cohesive but each have their own differences highlighting their specific divisions. This design will be specifically for the hot tub division. Colours to be used are, White, Blue, Black, Grey. The specific vehicle used is a 2022 Halvorden Kesta, please use that in the mockup. If not able to use a Kesta, please use a small SUV, but Kesta is definitely preferred.
Creative freedom is encouraged. Please include the following info as a minimum: Website, Phone, Email, Services Provided.

www.ferncrestpoolandspa.com
(604)555-0183
service@ferncrestpools.com

Services Provided:
*Weekly Maintenace.
*Repairs.
*Water Changes.

Target Market(s)

Mid to Upper Class Clientel with $200k+/year salary

Industry/Entity Type

Pool & Hot Tub Service - Weekly Water Maintenance & Repairs

Font styles to use
Sans Serif

Colors
0054AA
0677BA
7BADD7
CADEEF
E8F1F8
0094D4
00A9DD
6FCCEA
C7EBF8
E9F6FB
00AB8E
00BBA5
67D7C9
C6EFE9
E9F9F6

Requirements
Must have
• Our logo , services provided, contact info, website.
Should not have
• A bunch of text an clustered design

```html
<!DOCTYPE html>
<html lang="en">
<head>
<meta charset="utf-8">
<title>Ferncrest Pool &amp; Spa – Vehicle Wrap Layout</title>
<link rel="stylesheet" href="https://fonts.googleapis.com/css2?family=Montserrat:wght@700&family=Arimo:wght@400;700&display=swap">
<style>
  :root {
    --navy: #0d2a4a;
    --blue-deep: #0677BA;
    --blue-mid: #0094D4;
    --blue-bright: #00A9DD;
    --blue-soft: #6FCCEA;
    --phone-blue: #1b74b8;
    --ink: #1a1a1a;
    --white: #ffffff;
    --bg: #ffffff;
  }
  * { margin: 0; padding: 0; box-sizing: border-box; }
  html, body { width: 1200px; height: 927px; overflow: hidden; background: var(--bg); }
  .canvas { position: relative; width: 1200px; height: 927px; }
  .wrap-art { position: absolute; left: 0; top: 0; width: 1200px; height: 927px; }
  .side-label { position: absolute; inset: 0; }

  .contact { position: absolute; font-family: "Arimo", Arial, sans-serif; }
  .contact-phone { font-weight: 700; font-size: 21px; color: var(--phone-blue); letter-spacing: 0.2px; }
  .contact-email { font-size: 11px; color: var(--ink); letter-spacing: 0.4px; margin-top: 2px; }

  .brand { position: absolute; font-family: "Montserrat", sans-serif; font-weight: 700; color: var(--navy); line-height: 1; white-space: nowrap; }
  .brand-name { font-size: 32px; letter-spacing: 3px; display: block; }
  .brand-sub { font-size: 14px; letter-spacing: 8px; display: block; margin-top: 6px; }

  .web { position: absolute; font-family: "Arimo", Arial, sans-serif; font-weight: 700; font-size: 16px; color: var(--white); letter-spacing: -0.2px; white-space: nowrap; line-height: 18px; }

  .services { position: absolute; list-style: none; font-family: "Arimo", Arial, sans-serif; font-weight: 700; font-size: 12px; color: var(--navy); line-height: 16px; }
  .services li { white-space: nowrap; }
  .services--left li::before { content: ""; display: inline-block; width: 8px; height: 8px; border-radius: 50%; background: var(--white); margin-right: 5px; vertical-align: middle; }
  .services--right { text-align: right; }
  .services--right li::after { content: ""; display: inline-block; width: 8px; height: 8px; border-radius: 50%; background: var(--white); margin-left: 5px; vertical-align: middle; }
</style>
</head>
<body>
<main class="canvas">
  <svg class="wrap-art" viewBox="0 0 1200 927" xmlns="http://www.w3.org/2000/svg" aria-hidden="true">
    <g class="driver-side-graphics">
      <polygon points="390,352 830,340 830,378 390,378" fill="var(--blue-bright)"/>
      <polygon points="486,318 748,258 778,360 488,362" fill="var(--blue-mid)"/>
      <polygon points="755,222 905,160 940,205 800,215" fill="var(--blue-deep)"/>
      <polygon points="918,222 1000,168 1085,252 1040,262" fill="var(--blue-deep)"/>
      <polygon points="760,242 1040,262 1090,290 766,268" fill="var(--blue-bright)"/>
      <polygon points="772,285 1090,305 1085,330 778,305" fill="var(--blue-mid)"/>
      <polygon points="805,320 1070,318 1060,345 830,350" fill="var(--blue-soft)"/>
      <circle class="brand-dot" cx="440" cy="300" r="48" fill="var(--blue-mid)"/>
    </g>
    <g class="passenger-side-graphics">
      <polygon points="385,820 820,814 820,842 385,842" fill="var(--blue-bright)"/>
      <polygon points="446,718 712,768 704,830 418,830 420,800" fill="var(--blue-mid)"/>
      <polygon points="95,700 190,620 280,690 130,720" fill="var(--blue-deep)"/>
      <polygon points="265,655 295,610 445,670 300,668" fill="var(--blue-deep)"/>
      <polygon points="100,720 445,680 445,700 130,745" fill="var(--blue-bright)"/>
      <polygon points="100,752 445,705 445,712 115,775" fill="var(--blue-mid)"/>
      <polygon points="130,790 418,752 418,772 160,805" fill="var(--blue-soft)"/>
      <circle class="brand-dot" cx="762" cy="748" r="50" fill="var(--blue-mid)"/>
    </g>
  </svg>

  <section class="side-label side-label--driver">
    <div class="contact" style="left:211px; top:200px;">
      <div class="contact-phone">(604)555-0183</div>
      <div class="contact-email">service@ferncrestpools.com</div>
    </div>
    <div class="brand" style="left:504px; top:240px; transform:rotate(-11deg); transform-origin:left top;">
      <span class="brand-name">FERNCREST</span>
      <span class="brand-sub">POOL &amp; SPA</span>
    </div>
    <div class="web" style="left:496px; top:326px; transform:rotate(-12deg); transform-origin:left top;">www.ferncrestpoolandspa.com</div>
    <ul class="services services--left" style="left:588px; top:334px; transform:rotate(-11deg); transform-origin:left top;">
      <li>WEEKLY MAINTENACE</li>
      <li style="padding-left:45px;">WATER CHANGES</li>
      <li style="padding-left:110px;">REPAIRS</li>
    </ul>
  </section>

  <section class="side-label side-label--passenger">
    <div class="contact" style="left:814px; top:652px;">
      <div class="contact-phone">(604)555-0183</div>
      <div class="contact-email">service@ferncrestpools.com</div>
    </div>
    <div class="brand" style="left:462px; top:656px; transform:rotate(10deg); transform-origin:left top;">
      <span class="brand-name">FERNCREST</span>
      <span class="brand-sub">POOL &amp; SPA</span>
    </div>
    <div class="web" style="left:456px; top:734px; transform:rotate(10deg); transform-origin:left top;">www.ferncrestpoolandspa.com</div>
    <ul class="services services--right" style="left:426px; top:760px; width:190px; transform:rotate(10deg); transform-origin:left top;">
      <li>WEEKLY MAINTENACE</li>
      <li style="padding-right:45px;">WATER CHANGES</li>
      <li style="padding-right:110px;">REPAIRS</li>
    </ul>
  </section>
</main>
</body>
</html>
```